Web design for our new company

We need a web design for our product and for our company.
And the main is our Product tool called "velmora".
----------------------------------------------------------
[Our company's Goal]
Make organization’s communication smooth and healthy with transparency and efficiency for works and tasks in all levels with our workflow tool.

[Our Mission]
Our mission is to achieve business goals with customers.
We work together to identify the goals for your company, guides your strategy and bring the technology answers which best fit to achieve the goals.

[What we do]
We have a workflow tool "velmora"
- Very simple end-user configurable workflow for any company processes
(Targeting small-med size company)
- Graphical & fun features for startup users
- Simple and easy task control with quillbox e-mail look & feel
- Non charged skill up guidance
- Additional features with;
Multiple delegation
Clear status for each owner
Task owner management console with due date reminders&reporting

Others
1. System Development & Implementation Service
Our client list includes a wide variety of small to medium to major sized enterprises.
We can offer from full-scratch based development to packaged system implementation.

2. Project Management(PM) Service
We will provide end-to-end PM service with experienced PM.
Our service is not only “managing” but “leading” to bring success to achieve the goal.

3.Consultation Service

Consulting services to a wide range of fields such as creating business strategy, business process Kaizen, IT system consultation and change management.

Target Market(s)

Business to Business
Mainly to medium size - startup company

Industry/Entity Type

It Company

Coding

Coded - Design and coding required

Number of Pages Required

5+ page

Colors
0255a3
33a6d7
86cfc6
33b8a4
add136
cadf82
fbf289
fee18a
faa54b

Requirements
Must have
• We need Pages for
• Company mission
• Service Overview
• Contact
• Privacy Policy
• Terms and Conditions
• =========================
• As there were some questions, I add followings.---------
• 1. File Format
• We are going to use Brixel cloud services to upload finished web files.
• The finished files should be ready to use by simply replacing images and text.
• Please provide me "easy to handle" template with "sophisticated design".
• Thanks!
• 2. Multiple Languages
• We need buttons for changing language.
• We will have this translated to German, English and Japanese.
• Thank you so much!!
Nice to have
• These are current Logos and will be a next project to revise them...
• Attached Company Profile and Logo design
• 1. Company Profile
• 2. Our Company Logo
• 3. Our Product Logo -> This is most close to our image of design base.
• 4. Product Logo for PPT Header
• All just for your reference.
• ---------
• As there were some request, I added attachment as for contents for Our mission page.
Should not have
• I hope to see some unique designs.
• (Sorry please ignore my last update as I checked with our CEO.
• Bootstrap is absolutely good template.)

```html
<!DOCTYPE html>
<html lang="en">
<head>
<meta charset="utf-8">
<title>velmora — web design, two colour themes</title>
<link href="https://fonts.googleapis.com/css2?family=Montserrat:wght@400;500;600;700&family=Open+Sans:ital,wght@0,400;0,600;0,700;1,400&display=swap" rel="stylesheet">
<style>
:root{
  --board:#0e0f11;
  --side:#252a33;
  --band:#2d3340;
  --foot:#1d2128;
  --ink:#2b2f36;
  --muted:#8a8f97;
  --line:#e4e6ea;
  --blue:#33a6d7;
  --lime:#add136;
  --white:#ffffff;
}
*{margin:0;padding:0;box-sizing:border-box}
html,body{width:921px;height:1200px;overflow:hidden;background:var(--board)}
body{font-family:"Open Sans",Arial,sans-serif;color:var(--ink)}
.board{position:absolute;left:0;top:0;width:1151px;height:1500px;transform:scale(.8);transform-origin:0 0;background:var(--board)}
.page{position:absolute;top:70px;width:409px;height:1371px;background:var(--white);overflow:hidden}
.page--blue{left:103px;--accent:var(--blue)}
.page--lime{left:624px;--accent:var(--lime)}
.abs{position:absolute}
.sec{position:absolute;left:0;width:409px;overflow:hidden}
.h-title{position:absolute;left:0;width:100%;text-align:center;font-family:"Montserrat",sans-serif;font-weight:500;font-size:10.5px;letter-spacing:.6px;color:var(--ink)}
.rule{position:absolute;left:50%;width:30px;margin-left:-15px;height:1.5px;background:linear-gradient(90deg,var(--accent),#cadf82)}
.tiny{font-size:3.8px;line-height:6px;color:var(--muted)}

/* hero */
.hero{top:0;height:217px}
.sidebar{left:0;top:0;width:92px;height:217px;background:var(--side)}
.brand{left:14px;top:13px;width:28px;height:28px;background:var(--white);display:flex;align-items:center;justify-content:center;font-family:"Montserrat",sans-serif;font-weight:600;font-size:5px;color:var(--ink)}
.nav{left:16px;top:55px;width:56px;list-style:none}
.nav li{height:15px;font-family:"Montserrat",sans-serif;font-size:4.2px;font-weight:500;color:#d4d7dc;display:flex;justify-content:space-between;align-items:center}
.nav li.is-active{color:var(--accent)}
.nav li::after{content:"›";font-size:6px;color:#8a8f97}
.follow{left:18px;top:172px;font-size:4.5px;color:#c9ccd2}
.socials{left:17px;top:185px;display:flex;gap:4.5px}
.socials span{width:10px;height:10px;border:0.8px solid #c9ccd2;border-radius:50%}
.hero-photo{left:92px;top:0;width:317px;height:217px;background:linear-gradient(120deg,#dfe6ee 0%,#b9c7d4 40%,#6f8091 75%,#3d4a58 100%)}
.hero-kicker{left:115px;top:138px;width:156px;height:17px;background:rgba(255,255,255,.88);font-size:9.5px;color:#4a4f57;padding-left:13px;line-height:17px}
.hero-headline{left:122px;top:158px;width:234px;height:25px;background:var(--accent);font-family:"Montserrat",sans-serif;font-weight:700;font-size:10px;letter-spacing:.8px;color:var(--white);line-height:25px;text-align:center}

/* mission */
.mission{top:217px;height:178px}
.mission .lead{left:70px;top:50px;width:270px;text-align:center}
.svc{position:absolute;top:75px;width:110px;text-align:center}
.svc svg{display:block;margin:0 auto 6px}
.svc h3{font-family:"Montserrat",sans-serif;font-weight:600;font-size:5.2px;color:var(--ink);margin-bottom:4px}
.svc p{font-size:3.8px;line-height:6.5px;color:var(--muted)}

/* why */
.why{top:395px;height:168px}
.why-band{left:143px;top:0;width:266px;height:168px;background:var(--band)}
.why-photo{left:0;top:11px;width:184px;height:147px;background:linear-gradient(135deg,#b7c4cf,#7c8995 55%,#4b5560)}
.play{left:77px;top:74px}
.why h2{position:absolute;left:215px;top:31px;font-family:"Montserrat",sans-serif;font-weight:700;font-size:6.5px;letter-spacing:.5px;color:var(--white)}
.why-item{position:absolute;width:82px}
.why-item h4{font-size:5px;font-weight:600;color:var(--accent);margin-bottom:5px}
.why-item p{font-size:3.6px;line-height:6px;color:#aeb3bb}

/* blog */
.blog{top:563px;height:277px}
.post-main{left:33px;top:67px;width:235px;height:170px;border:1px solid #eceef1}
.post-main .ph{left:0;top:0;width:233px;height:101px;background:linear-gradient(120deg,#d7dde3,#a5b1bc 50%,#6a7682)}
.post-main h3{position:absolute;left:10px;top:113px;font-size:5.5px;font-weight:600;color:var(--ink)}
.post-main .ex{left:10px;top:126px;width:200px}
.meta{font-size:3.4px;color:var(--muted);display:flex;align-items:center;gap:3px}
.meta i{width:6px;height:6px;border-radius:50%;background:#c6cbd1;display:inline-block}
.plus{left:198px;top:145px;width:14px;height:14px;border-radius:50%;background:var(--accent);color:var(--white);font-size:9px;line-height:14px;text-align:center}
.post-side{position:absolute;left:279px;width:110px;height:34px}
.post-side .th{left:0;top:0;width:40px;height:33px;background:linear-gradient(135deg,#c5ced6,#7f8b97)}
.post-side h4{position:absolute;left:48px;top:2px;width:62px;font-size:4.2px;line-height:6px;font-weight:600;color:var(--ink)}
.post-side .meta{position:absolute;left:48px;top:18px}

/* testimonial */
.happy{top:840px;height:155px;background:linear-gradient(90deg,#6a5546 0%,#5a6b80 35%,#8a6e5c 60%,#5b4a40 100%)}
.quote{left:199px;top:30px;width:173px;height:110px;background:var(--band)}
.quote h2{position:absolute;left:21px;top:17px;font-family:"Montserrat",sans-serif;font-weight:500;font-size:10px;letter-spacing:1px;color:var(--white)}
.quote .txt{left:21px;top:44px;width:130px;font-style:italic;font-size:3.8px;line-height:6px;color:#aeb3bb}
.quote .name{left:21px;top:74px;font-size:5.5px;color:var(--white)}
.quote .loc{left:21px;top:84px;font-size:3.8px;font-style:italic;color:#aeb3bb}
.pill{left:124px;top:84px;width:32px;height:10px;border-radius:5px;background:var(--accent);color:var(--white);font-size:6px;line-height:10px;text-align:center;letter-spacing:4px}

/* clients */
.clients{top:995px;height:109px}
.logos{left:43px;top:50px;display:flex;gap:11px}
.logos span{width:59px;height:30px;border:1px solid #eef0f2;display:flex;align-items:center;justify-content:center;font-size:5.5px;font-weight:600;color:#8a8f97}

/* cta */
.cta{top:1104px;height:96px;background:var(--accent)}
.cta p{position:absolute;left:0;top:25px;width:100%;text-align:center;font-family:"Montserrat",sans-serif;font-weight:500;font-size:10px;line-height:13px;letter-spacing:.6px;color:var(--ink)}
.cta .btn{left:162px;top:62px;width:107px;height:14px;border:1px solid var(--ink);font-family:"Montserrat",sans-serif;font-weight:600;font-size:4.5px;line-height:12px;text-align:center;color:var(--ink)}

/* footer */
.footer{top:1200px;height:171px;background:var(--foot)}
.fcol{position:absolute;top:28px}
.fcol h5{font-family:"Montserrat",sans-serif;font-weight:500;font-size:6px;color:var(--white);margin-bottom:8px}
.fcol li{list-style:none;font-size:3.6px;line-height:11px;color:#7c828d}
.fcol .row{display:flex;gap:4px;align-items:flex-start;font-size:3.6px;line-height:6px;color:#7c828d;margin-bottom:6px}
.fcol .row svg{flex:none;margin-top:1px}
.news{display:flex;width:114px;height:13px}
.news span{flex:1;background:#353a44;font-size:3.4px;line-height:13px;color:#7c828d;padding-left:14px}
.news b{width:37px;background:var(--accent);font-size:3.4px;line-height:13px;text-align:center;color:var(--white)}
.fsoc{display:flex;gap:4px;margin-top:6px}
.fsoc i{width:10px;height:10px;border-radius:50%;display:block}
.copy{left:0;top:150px;width:100%;text-align:center;font-size:3.6px;color:#6a707b}
</style>
</head>
<body>
<div class="board">

<!-- ===== theme: blue ===== -->
<article class="page page--blue">
  <section class="sec hero">
    <div class="abs hero-photo" role="img" aria-label="Photo of two colleagues discussing work at an office desk"></div>
    <div class="abs sidebar"></div>
    <div class="abs brand">velmora</div>
    <ul class="abs nav"><li class="is-active">HOME</li><li>SERVICE</li><li>ABOUT US</li><li>PRODUCT</li><li>PRICING</li><li>POLICY</li><li>CONTACT US</li></ul>
    <div class="abs follow">Follow Us :</div>
    <div class="abs socials"><span></span><span></span><span></span><span></span></div>
    <div class="abs hero-kicker">Our Mission is to Achieve</div>
    <div class="abs hero-headline">BUSINESS GOALS WITH CUSTOMERS .</div>
  </section>

  <section class="sec mission">
    <h2 class="h-title" style="top:24px">OUR MISSION</h2>
    <div class="rule" style="top:41px"></div>
    <p class="abs tiny lead">Our mission is to achieve business goals with customers. We work together to identify the goals for your company, guides your strategy and bring the technology answers which best fit to achieve the goals.</p>
    <div class="svc" style="left:24px">
      <svg width="22" height="20" viewBox="0 0 22 20" fill="none" stroke="var(--accent)" stroke-width="1"><rect x="3" y="2" width="15" height="13"/><path d="M6 12l3-4 3 2 4-5"/><path d="M1 18h20"/></svg>
      <h3>Project Management(PM) Service</h3>
      <p>We will provide end-to-end PM service with experienced PM. Our service is not only "Managing" but "Leading" to bring success to achieve the goal.</p>
    </div>
    <div class="svc" style="left:149px">
      <svg width="22" height="20" viewBox="0 0 22 20" fill="none" stroke="var(--accent)" stroke-width="1"><rect x="2" y="8" width="5" height="10"/><rect x="9" y="3" width="5" height="15"/><rect x="16" y="6" width="4" height="12"/></svg>
      <h3>System Development &amp; Implementation</h3>
      <p>Our client list includes a wide variety of small to medium to major sized enterprises. We can offer from full-scratch based development to packaged system.</p>
    </div>
    <div class="svc" style="left:264px">
      <svg width="22" height="20" viewBox="0 0 22 20" fill="none" stroke="var(--accent)" stroke-width="1"><circle cx="11" cy="5" r="3"/><circle cx="4" cy="15" r="3"/><circle cx="18" cy="15" r="3"/><path d="M9 7l-3 6M13 7l3 6M7 15h8"/></svg>
      <h3>Consultation Service</h3>
      <p>Consulting services to a wide range of fields such as creating business strategy, business process Kaizen, IT system consultation and</p>
    </div>
  </section>

  <section class="sec why">
    <div class="abs why-band"></div>
    <div class="abs why-photo" role="img" aria-label="Video still of a team talking by a window"></div>
    <svg class="abs play" width="22" height="22" viewBox="0 0 22 22" fill="none" stroke="var(--accent)" stroke-width="1.4"><circle cx="11" cy="11" r="10"/><path d="M9 7l6 4-6 4z"/></svg>
    <h2>WHY CHOOSE US</h2>
    <div class="why-item" style="left:217px;top:62px"><h4>Customer Support</h4><p>There are many variations of passages of text but the majority have taken changes form.</p></div>
    <div class="why-item" style="left:307px;top:62px"><h4>Bulk SMS</h4><p>All the sample text on the web tend to repeat predefined chunks where necessary.</p></div>
    <div class="why-item" style="left:217px;top:111px"><h4>Money Exchange</h4><p>There are many variations of passages of text but the majority have taken changes form.</p></div>
    <div class="why-item" style="left:307px;top:111px"><h4>Business Boosting</h4><p>There are many variations of passages of text but the majority have taken changes form.</p></div>
  </section>

  <section class="sec blog">
    <h2 class="h-title" style="top:28px">LATEST BLOG</h2>
    <div class="rule" style="top:45px"></div>
    <div class="abs post-main">
      <div class="abs ph" role="img" aria-label="Blog photo of a coach meeting with an entrepreneur"></div>
      <h3>Why Would a Successful Entrepreneur Hire a Coach?</h3>
      <p class="abs tiny ex">Our mission is to achieve business goals with customers. We work together to identify the goals for your company, guides your strategy.</p>
      <div class="abs meta" style="left:10px;top:155px"><i></i>BY ADMIN &nbsp;|&nbsp; FEB 15, 2017</div>
      <div class="abs plus">+</div>
    </div>
    <div class="post-side" style="top:69px"><div class="abs th" role="img" aria-label="Blog thumbnail photo"></div><h4>Successful Entrepreneur Hire a Coach?</h4><div class="meta"><i></i>BY ADMIN | FEB 15, 2017</div></div>
    <div class="post-side" style="top:113px"><div class="abs th" role="img" aria-label="Blog thumbnail photo"></div><h4>Successful Entrepreneur Hire a Coach?</h4><div class="meta"><i></i>BY ADMIN | FEB 15, 2017</div></div>
    <div class="post-side" style="top:156px"><div class="abs th" role="img" aria-label="Blog thumbnail photo"></div><h4>Successful Entrepreneur Hire a Coach?</h4><div class="meta"><i></i>BY ADMIN | FEB 15, 2017</div></div>
    <div class="post-side" style="top:200px"><div class="abs th" role="img" aria-label="Blog thumbnail photo"></div><h4>Successful Entrepreneur Hire a Coach?</h4><div class="meta"><i></i>BY ADMIN | FEB 15, 2017</div></div>
  </section>

  <section class="sec happy" role="img" aria-label="Portrait photo of a smiling client in front of a brick wall">
    <div class="abs quote">
      <h2>HAPPY CLIENTS</h2>
      <p class="abs txt">There are many variations of passages of text available, but the majority have suffered alteration. There are many variations of passages of text.</p>
      <div class="abs name">CLARA WENDT</div>
      <div class="abs loc">Manhattan, New York</div>
      <div class="abs pill">‹›</div>
    </div>
  </section>

  <section class="sec clients">
    <h2 class="h-title" style="top:24px">OUR CLIENTS</h2>
    <div class="abs logos"><span>Vantora</span><span>Crestline</span><span>Halden Finance</span><span>Nordvik</span><span>Synthwell</span></div>
  </section>

  <section class="sec cta">
    <p>Our Mission is to Achieve Business<br>Goals with Customers</p>
    <div class="abs btn">WORK WITH US TODAY</div>
  </section>

  <footer class="sec footer">
    <div class="fcol" style="left:21px;width:86px">
      <h5>Contact Us</h5>
      <div class="row"><svg width="4" height="5" viewBox="0 0 4 5"><path d="M2 5C.5 3 0 2.3 0 1.8a2 2 0 014 0C4 2.3 3.5 3 2 5z" fill="#c9ccd2"/></svg>Linden road, Harbor Street 220-90, Maple Town, Your Country</div>
      <div class="row"><svg width="4" height="4" viewBox="0 0 4 4"><path d="M0 1c0 1.6 1.4 3 3 3l1-1-1-1-.6.5C1.8 2.2 1.8 2.2 1.5 1.6L2 1 1 0z" fill="#c9ccd2"/></svg>(300) 555 0142, (300) 555 0176</div>
      <div class="row"><svg width="5" height="4" viewBox="0 0 5 4"><rect width="5" height="4" fill="#c9ccd2"/></svg>hello@velmora.co</div>
      <div class="row"><svg width="4" height="4" viewBox="0 0 4 4"><circle cx="2" cy="2" r="2" fill="#c9ccd2"/></svg>Monday - Friday 09:00 - 18:00 Saturday, Sunday Closed</div>
    </div>
    <div class="fcol" style="left:116px"><h5>Quick Link</h5><ul><li>About us</li><li>Services</li><li>Career</li><li>Projects</li><li>Blog</li><li>Contact</li></ul></div>
    <div class="fcol" style="left:180px"><h5>Services</h5><ul><li>Customer Support</li><li>Bulk sms service</li><li>Business boosting</li><li>Money exchange</li><li>Consulting Services</li><li>Strategic Planning</li><li>International</li></ul></div>
    <div class="fcol" style="left:275px">
      <h5>Newsletter</h5>
      <div class="tiny" style="margin:-4px 0 4px">Enter your email &amp; subscribe newsletter</div>
      <div class="news"><span>Email address</span><b>SUBSCRIBE</b></div>
      <h5 style="margin-top:18px;margin-bottom:2px">Contact us on</h5>
      <div class="fsoc"><i style="background:#3b5998"></i><i style="background:#5a7fa8"></i><i style="background:#dd4b39"></i><i style="background:#e4407a"></i><i style="background:#2aa3ef"></i></div>
    </div>
    <div class="abs copy">2018 all rights reserved</div>
  </footer>
</article>

<!-- ===== theme: lime ===== -->
<article class="page page--lime">
  <section class="sec hero">
    <div class="abs hero-photo" role="img" aria-label="Photo of colleagues in a lively discussion" style="background:linear-gradient(120deg,#e6ebef 0%,#c3ccd4 40%,#7d8c99 75%,#46525e 100%)"></div>
    <div class="abs sidebar"></div>
    <div class="abs brand">velmora</div>
    <ul class="abs nav"><li class="is-active">HOME</li><li>SERVICE</li><li>ABOUT US</li><li>PRODUCT</li><li>PRICING</li><li>POLICY</li><li>CONTACT US</li></ul>
    <div class="abs follow">Follow Us :</div>
    <div class="abs socials"><span></span><span></span><span></span><span></span></div>
    <div class="abs hero-kicker">Our Mission is to Achieve</div>
    <div class="abs hero-headline" style="color:var(--ink)">BUSINESS GOALS WITH CUSTOMERS .</div>
  </section>

  <section class="sec mission">
    <h2 class="h-title" style="top:24px">OUR MISSION</h2>
    <div class="rule" style="top:41px"></div>
    <p class="abs tiny lead">Our mission is to achieve business goals with customers. We work together to identify the goals for your company, guides your strategy and bring the technology answers which best fit to achieve the goals.</p>
    <div class="svc" style="left:24px">
      <svg width="22" height="20" viewBox="0 0 22 20" fill="none" stroke="var(--accent)" stroke-width="1"><rect x="3" y="2" width="15" height="13"/><path d="M6 12l3-4 3 2 4-5"/><path d="M1 18h20"/></svg>
      <h3>Project Management(PM) Service</h3>
      <p>We will provide end-to-end PM service with experienced PM. Our service is not only "Managing" but "Leading" to bring success to achieve the goal.</p>
    </div>
    <div class="svc" style="left:149px">
      <svg width="22" height="20" viewBox="0 0 22 20" fill="none" stroke="var(--accent)" stroke-width="1"><rect x="2" y="8" width="5" height="10"/><rect x="9" y="3" width="5" height="15"/><rect x="16" y="6" width="4" height="12"/></svg>
      <h3>System Development &amp; Implementation</h3>
      <p>Our client list includes a wide variety of small to medium to major sized enterprises. We can offer from full-scratch based development to packaged system.</p>
    </div>
    <div class="svc" style="left:264px">
      <svg width="22" height="20" viewBox="0 0 22 20" fill="none" stroke="var(--accent)" stroke-width="1"><circle cx="11" cy="5" r="3"/><circle cx="4" cy="15" r="3"/><circle cx="18" cy="15" r="3"/><path d="M9 7l-3 6M13 7l3 6M7 15h8"/></svg>
      <h3>Consultation Service</h3>
      <p>Consulting services to a wide range of fields such as creating business strategy, business process Kaizen, IT system consultation and</p>
    </div>
  </section>

  <section class="sec why">
    <div class="abs why-band"></div>
    <div class="abs why-photo" role="img" aria-label="Video still of a group of colleagues talking" style="background:linear-gradient(135deg,#cfc8bd,#8d8a85 55%,#4b4f55)"></div>
    <svg class="abs play" width="22" height="22" viewBox="0 0 22 22" fill="none" stroke="var(--accent)" stroke-width="1.4"><circle cx="11" cy="11" r="10"/><path d="M9 7l6 4-6 4z"/></svg>
    <h2>WHY CHOOSE US</h2>
    <div class="why-item" style="left:217px;top:62px"><h4>Customer Support</h4><p>There are many variations of passages of text but the majority have taken changes form.</p></div>
    <div class="why-item" style="left:307px;top:62px"><h4>Bulk SMS</h4><p>All the sample text on the web tend to repeat predefined chunks where necessary.</p></div>
    <div class="why-item" style="left:217px;top:111px"><h4>Money Exchange</h4><p>There are many variations of passages of text but the majority have taken changes form.</p></div>
    <div class="why-item" style="left:307px;top:111px"><h4>Business Boosting</h4><p>There are many variations of passages of text but the majority have taken changes form.</p></div>
  </section>

  <section class="sec blog">
    <h2 class="h-title" style="top:28px">LATEST BLOG</h2>
    <div class="rule" style="top:45px"></div>
    <div class="abs post-main">
      <div class="abs ph" role="img" aria-label="Blog photo of a coach meeting with an entrepreneur"></div>
      <h3>Why Would a Successful Entrepreneur Hire a Coach?</h3>
      <p class="abs tiny ex">Our mission is to achieve business goals with customers. We work together to identify the goals for your company, guides your strategy.</p>
      <div class="abs meta" style="left:10px;top:155px"><i></i>BY ADMIN &nbsp;|&nbsp; FEB 15, 2017</div>
      <div class="abs plus">+</div>
    </div>
    <div class="post-side" style="top:69px"><div class="abs th" role="img" aria-label="Blog thumbnail photo"></div><h4>Successful Entrepreneur Hire a Coach?</h4><div class="meta"><i></i>BY ADMIN | FEB 15, 2017</div></div>
    <div class="post-side" style="top:113px"><div class="abs th" role="img" aria-label="Blog thumbnail photo"></div><h4>Successful Entrepreneur Hire a Coach?</h4><div class="meta"><i></i>BY ADMIN | FEB 15, 2017</div></div>
    <div class="post-side" style="top:156px"><div class="abs th" role="img" aria-label="Blog thumbnail photo"></div><h4>Successful Entrepreneur Hire a Coach?</h4><div class="meta"><i></i>BY ADMIN | FEB 15, 2017</div></div>
    <div class="post-side" style="top:200px"><div class="abs th" role="img" aria-label="Blog thumbnail photo"></div><h4>Successful Entrepreneur Hire a Coach?</h4><div class="meta"><i></i>BY ADMIN | FEB 15, 2017</div></div>
  </section>

  <section class="sec happy" role="img" aria-label="Portrait photo of a smiling client in front of a brick wall">
    <div class="abs quote">
      <h2>HAPPY CLIENTS</h2>
      <p class="abs txt">There are many variations of passages of text available, but the majority have suffered alteration. There are many variations of passages of text.</p>
      <div class="abs name">CLARA WENDT</div>
      <div class="abs loc">Manhattan, New York</div>
      <div class="abs pill">‹›</div>
    </div>
  </section>

  <section class="sec clients">
    <h2 class="h-title" style="top:24px">OUR CLIENTS</h2>
    <div class="abs logos"><span>Vantora</span><span>Crestline</span><span>Halden Finance</span><span>Nordvik</span><span>Synthwell</span></div>
  </section>

  <section class="sec cta">
    <p>Our Mission is to Achieve Business<br>Goals with Customers</p>
    <div class="abs btn">WORK WITH US TODAY</div>
  </section>

  <footer class="sec footer">
    <div class="fcol" style="left:21px;width:86px">
      <h5>Contact Us</h5>
      <div class="row"><svg width="4" height="5" viewBox="0 0 4 5"><path d="M2 5C.5 3 0 2.3 0 1.8a2 2 0 014 0C4 2.3 3.5 3 2 5z" fill="#c9ccd2"/></svg>Linden road, Harbor Street 220-90, Maple Town, Your Country</div>
      <div class="row"><svg width="4" height="4" viewBox="0 0 4 4"><path d="M0 1c0 1.6 1.4 3 3 3l1-1-1-1-.6.5C1.8 2.2 1.8 2.2 1.5 1.6L2 1 1 0z" fill="#c9ccd2"/></svg>(300) 555 0142, (300) 555 0176</div>
      <div class="row"><svg width="5" height="4" viewBox="0 0 5 4"><rect width="5" height="4" fill="#c9ccd2"/></svg>hello@velmora.co</div>
      <div class="row"><svg width="4" height="4" viewBox="0 0 4 4"><circle cx="2" cy="2" r="2" fill="#c9ccd2"/></svg>Monday - Friday 09:00 - 18:00 Saturday, Sunday Closed</div>
    </div>
    <div class="fcol" style="left:116px"><h5>Quick Link</h5><ul><li>About us</li><li>Services</li><li>Career</li><li>Projects</li><li>Blog</li><li>Contact</li></ul></div>
    <div class="fcol" style="left:180px"><h5>Services</h5><ul><li>Customer Support</li><li>Bulk sms service</li><li>Business boosting</li><li>Money exchange</li><li>Consulting Services</li><li>Strategic Planning</li><li>International</li></ul></div>
    <div class="fcol" style="left:275px">
      <h5>Newsletter</h5>
      <div class="tiny" style="margin:-4px 0 4px">Enter your email &amp; subscribe newsletter</div>
      <div class="news"><span>Email address</span><b>SUBSCRIBE</b></div>
      <h5 style="margin-top:18px;margin-bottom:2px">Contact us on</h5>
      <div class="fsoc"><i style="background:#3b5998"></i><i style="background:#5a7fa8"></i><i style="background:#dd4b39"></i><i style="background:#e4407a"></i><i style="background:#2aa3ef"></i></div>
    </div>
    <div class="abs copy">2018 all rights reserved</div>
  </footer>
</article>

</div>
</body>
</html>
```